Hearth of the Heron: Half-Page Magazine Ad

advertisement in a travel magazine for a casual/fine dining restaurant in the heart of Whitehorse, Yukon
Needs to say that it is located in the Stonereach Hotel, 247 Larch Avenue.

Northern inspired cuisine
hearthoftheheron-example.ca

Don't need to use all the pictures

Dimensions: ad is a half-page, dimensions are 7.25" x 4.8".

Target Market(s)

Upscale dining, corporate travellers

Industry/Entity Type

Restaurant

Colors
0054AA
0677BA
7BADD7
CADEEF
E8F1F8
0094D4
00A9DD
6FCCEA
C7EBF8
E9F6FB
00AB8E
00BBA5
67D7C9
C6EFE9
E9F9F6

Requirements
Must have
• Restaurant logo
Nice to have
• Simple, clean design with upscale feel

```html
<!DOCTYPE html>
<html lang="en">
<head>
<meta charset="utf-8">
<title>Hearth of the Heron — Half-Page Ad</title>
<link rel="stylesheet" href="https://fonts.googleapis.com/css2?family=Montserrat:wght@500;600&display=swap">
<style>
  :root {
    --stage: #e4e6e9;
    --paper: #f6f7f8;
    --wave-tone: #eceeef;
    --brand-blue: #0054AA;
    --ink-grey: #8a8c8f;
    --ink-dark: #1c1c1c;
    --white: #ffffff;
    --dish-warm: #d9772c;
    --dish-deep: #a9481c;
    --dish-green: #7a9b3a;
  }
  * { margin: 0; padding: 0; box-sizing: border-box; }
  html, body {
    width: 1200px; height: 849px; overflow: hidden;
    background: var(--stage);
    font-family: "Montserrat", Arial, sans-serif;
  }
  .ad {
    position: absolute; left: 0; top: 27px;
    width: 1200px; height: 795px;
    background: linear-gradient(135deg, var(--paper) 0%, var(--wave-tone) 50%, var(--paper) 100%);
    overflow: hidden;
  }
  .dish-photo {
    position: absolute; left: 0; top: 46px;
    width: 492px; height: 669px;
    background: radial-gradient(circle at 45% 45%, var(--dish-green) 0%, var(--dish-warm) 35%, var(--dish-deep) 100%);
  }
  .brand-mark {
    position: absolute; left: 578px; top: 86px;
    width: 260px; height: 197px;
    background: var(--white);
    display: flex; align-items: center; justify-content: center;
    text-align: center;
  }
  .brand-name {
    font-weight: 600; font-size: 30px; line-height: 1.15;
    letter-spacing: 0.04em; text-transform: uppercase;
    color: var(--ink-dark);
  }
  .copy { position: absolute; left: 709px; }
  .tagline {
    font-weight: 500; font-size: 19px; line-height: 25px;
    letter-spacing: 0.06em; color: var(--ink-grey);
    text-transform: uppercase;
  }
  .tagline--intro { top: 319px; }
  .tagline--cuisine { top: 602px; }
  .city {
    top: 422px;
    font-weight: 600; font-size: 40px; line-height: 44px;
    letter-spacing: 0.03em; color: var(--brand-blue);
  }
  .address-band {
    position: absolute; left: 696px; top: 517px;
    width: 504px; height: 72px;
    background: var(--brand-blue);
    padding: 9px 0 0 13px;
    font-weight: 600; font-size: 20px; line-height: 25px;
    letter-spacing: 0.04em; color: var(--white);
  }
  .web {
    top: 712px;
    font-weight: 600; font-size: 19px;
    letter-spacing: 0.1em; color: var(--brand-blue);
  }
</style>
</head>
<body>
  <main class="ad">
    <div class="dish-photo" role="img" aria-label="Close-up photo of a plated pasta dish with ragù, shaved cheese and microgreens"></div>

    <div class="brand-mark">
      <p class="brand-name">Hearth<br>of the<br>Heron</p>
    </div>

    <p class="copy tagline tagline--intro">Fine dining<br>restaurant<br>in the<br>heart of</p>
    <h1 class="copy city">WHITEHORSE,<br>YUKON</h1>

    <p class="address-band">STONEREACH HOTEL,<br>247 LARCH AVENUE</p>

    <p class="copy tagline tagline--cuisine">Northern<br>inspired<br>cuisine</p>
    <p class="copy web">hearthoftheheron-example.ca</p>
  </main>
</body>
</html>
```